Broschüre für Tierarztpraxis
Zielgruppe
Wir sind eine Tierarztpraxis. Meine Zielgruppe sind hauptsächlich Hunde- und Katzenbesitzer. Wir behandeln auch Hühner und kleine Heimtiere (Kaninchen und Meerschweinchen) ambulant.
Aufgabenstellung
Wir sehen uns als 1. Anlaufstelle für tiermedizinische Probleme bei Haustieren. Wir bieten 24/7 Notfalldienst (einzigartig in unserer Region) sowie persönliche Betreuung durch kleines Team.
Neu bieten wir Zahnsanierung an die wir dank neuem dentalröntgen sehr professionell und kompetent erledigen können (sollte hervorgehoben werden als NEUE Dienstleistung. Speziell ist auch, dass wir Hühner ambulant in unsere Praxis ( Sprechstunde) betreuen.
Ein Foto von mir als Praxisinhaberin und (Haupt) Tierärztin für Kleintiere sollte rein- ich muss dies aber erst machen lassen

```html
<!DOCTYPE html>
<html lang="de">
<head>
<meta charset="utf-8">
<title>Tierarztpraxis Lindenau – Broschüre</title>
<link href="https://fonts.googleapis.com/css2?family=Poppins:wght@400;500;600;700&display=swap" rel="stylesheet">
<style>
  :root{
    --bg:#ebe8e3;
    --paper:#f8f7f5;
    --fold:#e7e4e0;
    --brown:#7b5c4a;
    --tan:#c8ac97;
    --sand:#e4d3c4;
    --accent:#d69a62;
    --ink:#2a2725;
    --muted:#4d4845;
  }
  *{box-sizing:border-box;margin:0;padding:0}
  html,body{width:1200px;height:780px;overflow:hidden}
  body{background:var(--bg);font-family:"Poppins",sans-serif;color:var(--ink);position:relative}

  .brochure{position:absolute;width:480px;height:340px;background:var(--paper);overflow:hidden;
    box-shadow:0 6px 18px rgba(0,0,0,.12)}
  .brochure--outside{left:90px;top:60px}
  .brochure--inside{left:630px;top:380px}
  .brochure__shapes{position:absolute;inset:0;width:100%;height:100%}
  .fold{position:absolute;top:0;bottom:0;width:1px;background:var(--fold);z-index:3}
  .fold--1{left:160px}.fold--2{left:320px}

  .panel{position:absolute;top:0;width:160px;height:100%;z-index:2}
  .panel--1{left:0}.panel--2{left:160px}.panel--3{left:320px}

  .photo{position:absolute;z-index:1}
  .photo--animals{left:0;right:6px;top:252px;bottom:4px;border-radius:60px 80px 0 0;
    background:linear-gradient(90deg,#b9926c,#8d6b52 30%,#d9c0a0 55%,#b48660 78%,#cdb394)}
  .photo--dog{left:18px;top:160px;width:105px;height:180px;border-radius:50px 50px 0 0;
    background:linear-gradient(180deg,#8a5a3e,#6e4330 70%,#5a3a2c)}
  .photo--cat{left:300px;top:0;width:180px;height:170px;border-radius:95px 0 0 95px/85px 0 0 85px;
    background:radial-gradient(circle at 45% 45%,#e9c7a4,#d5a982 55%,#8fa1b4)}

  /* outside */
  .brand-line{font-weight:600;font-size:8px;color:var(--accent);text-align:center;margin-top:32px;letter-spacing:.2px}
  .contacts__title{font-weight:500;font-size:13px;text-align:center;margin:16px 0 12px}
  .contacts__list{list-style:none;padding-left:20px}
  .contacts__item{display:flex;align-items:center;gap:5px;font-size:6.4px;margin-bottom:5px;color:var(--ink)}
  .contacts__icon{width:7px;height:7px;flex:none}

  .why__title{font-weight:500;font-size:13px;text-align:center;margin-top:40px}
  .why__text{font-size:5.9px;line-height:1.6;color:var(--muted);padding:0 12px;margin-top:14px}
  .bubble{position:absolute;left:76px;top:150px;width:48px;height:44px;z-index:4}
  .bubble__text{position:absolute;inset:0;display:flex;align-items:center;justify-content:center;text-align:center;
    font-weight:600;font-size:7.5px;line-height:1.1;color:var(--brown);padding-bottom:4px}

  .cover__name{position:absolute;top:98px;left:0;right:0;text-align:center;font-weight:700;font-size:13px;color:var(--ink);
    display:flex;align-items:center;justify-content:center;gap:6px}
  .cover__dot{width:8px;height:8px;border-radius:50%;background:var(--accent)}

  /* inside */
  .emergency__title{font-weight:500;font-size:12.5px;margin:56px 0 0 11px}
  .emergency__text{font-size:4.6px;line-height:1.5;color:var(--muted);margin:6px 12px 0 11px}
  .emergency__phone{display:flex;align-items:center;gap:4px;font-size:6.4px;margin:6px 0 0 11px}

  .services__title{font-weight:500;font-size:12.5px;text-align:center;line-height:1.35;margin-top:82px}
  .services__list{list-style:none;padding:10px 10px 0 8px}
  .service{margin-bottom:9px}
  .service__name{font-weight:700;font-size:5.6px}
  .service__text{font-size:4.5px;line-height:1.55;color:var(--muted);margin-top:2px}
  .services__url{position:absolute;bottom:11px;left:0;right:0;text-align:center;font-size:5.6px;color:var(--muted)}

  .care__title{font-weight:500;font-size:10.5px;line-height:1.35;margin:184px 0 0 12px}
  .care__list{list-style:none;margin:10px 10px 0 12px}
  .care__item{font-size:5.8px;line-height:1.5;margin-bottom:6px;padding-left:6px;position:relative}
  .care__item::before{content:"•";position:absolute;left:0}
  .care__item b{font-weight:700}
</style>
</head>
<body>

<!-- Aussenseite -->
<section class="brochure brochure--outside">
  <svg class="brochure__shapes" viewBox="0 0 480 340" preserveAspectRatio="none">
    <path d="M0 228 C60 212 120 222 180 246 C260 280 360 268 480 246 L480 340 L0 340Z" fill="var(--brown)"/>
    <path d="M0 282 C90 262 180 268 260 294 C340 316 420 298 480 286 L480 340 L0 340Z" fill="var(--sand)"/>
  </svg>
  <div class="photo photo--animals" role="img" aria-label="Gruppenfoto von Welpen, Kätzchen, Kaninchen und Meerschweinchen"></div>
  <span class="fold fold--1"></span><span class="fold fold--2"></span>

  <div class="panel panel--1 contacts">
    <p class="brand-line">Tierarztpraxis Lindenau</p>
    <h2 class="contacts__title">Kontakte</h2>
    <ul class="contacts__list">
      <li class="contacts__item"><svg class="contacts__icon" viewBox="0 0 10 10"><circle cx="5" cy="5" r="5" fill="var(--brown)"/><path d="M5 2.2a1.8 1.8 0 0 0-1.8 1.8c0 1.4 1.8 3.6 1.8 3.6S6.8 5.4 6.8 4A1.8 1.8 0 0 0 5 2.2z" fill="#fff"/></svg>Talstrasse 12, 3150 Mittelau</li>
      <li class="contacts__item"><svg class="contacts__icon" viewBox="0 0 10 10"><circle cx="5" cy="5" r="5" fill="var(--brown)"/><path d="M3.2 2.6l1 .1.4 1.2-.6.5a3.5 3.5 0 0 0 1.6 1.6l.5-.6 1.2.4.1 1-.7.5C4.9 7.2 2.8 5.1 2.7 3.3z" fill="#fff"/></svg>031 555 27 40</li>
      <li class="contacts__item"><svg class="contacts__icon" viewBox="0 0 10 10"><circle cx="5" cy="5" r="5" fill="var(--brown)"/><rect x="2.6" y="3.3" width="4.8" height="3.4" fill="none" stroke="#fff" stroke-width=".7"/><path d="M2.6 3.4L5 5.3l2.4-1.9" fill="none" stroke="#fff" stroke-width=".7"/></svg>hallo@praxis-lindenau.ch</li>
      <li class="contacts__item"><svg class="contacts__icon" viewBox="0 0 10 10"><circle cx="5" cy="5" r="5" fill="var(--brown)"/><circle cx="5" cy="5" r="2.3" fill="none" stroke="#fff" stroke-width=".7"/><path d="M2.7 5h4.6" stroke="#fff" stroke-width=".6"/></svg>tierarztpraxis-lindenau.ch</li>
    </ul>
  </div>

  <div class="panel panel--2 why">
    <h2 class="why__title">Warum zu uns?</h2>
    <p class="why__text">Unsere engagierten Tierärzte und Fachleute stehen für die Gesundheit und das Wohlbefinden Ihrer Tiere ein. Verlassen Sie sich auf unsere Erfahrung und Hingabe!</p>
    <div class="bubble">
      <svg viewBox="0 0 48 44" width="48" height="44"><circle cx="25" cy="20" r="19" fill="var(--tan)"/><path d="M10 30 L6 42 L18 36Z" fill="var(--tan)"/></svg>
      <p class="bubble__text">24H Für<br>Sie da</p>
    </div>
  </div>

  <div class="panel panel--3 cover">
    <h1 class="cover__name"><span class="cover__dot"></span>Tierarztpraxis Lindenau</h1>
  </div>
</section>

<!-- Innenseite -->
<section class="brochure brochure--inside">
  <svg class="brochure__shapes" viewBox="0 0 480 340" preserveAspectRatio="none">
    <path d="M0 0 H340 C310 40 270 72 210 76 C140 80 70 26 0 14Z" fill="var(--sand)"/>
    <path d="M0 14 C70 26 140 80 210 76 C270 72 310 40 340 0 H330 C300 34 262 62 210 66 C140 70 70 14 0 4Z" fill="var(--brown)"/>
    <path d="M0 262 C40 250 90 262 130 284 C200 318 330 300 480 290 L480 340 L0 340Z" fill="var(--brown)"/>
    <path d="M0 300 C80 290 170 300 260 314 C340 326 420 312 480 304 L480 340 L0 340Z" fill="var(--sand)"/>
    <rect x="320" y="300" width="160" height="40" fill="var(--tan)" opacity=".6"/>
  </svg>
  <div class="photo photo--dog" role="img" aria-label="Foto eines braunen Hundes mit Stethoskop"></div>
  <div class="photo photo--cat" role="img" aria-label="Foto einer Katze bei der Zahnkontrolle durch die Tierärztin"></div>
  <span class="fold fold--1"></span><span class="fold fold--2"></span>

  <div class="panel panel--1 emergency">
    <h2 class="emergency__title">Notfallkommunikation</h2>
    <p class="emergency__text">Für dringende Notfälle, hinterlassen Sie eine Nachricht – wir sind bemüht, schnellstmöglich zu reagieren.</p>
    <p class="emergency__phone"><svg width="7" height="7" viewBox="0 0 10 10"><circle cx="5" cy="5" r="5" fill="var(--brown)"/><path d="M3.2 2.6l1 .1.4 1.2-.6.5a3.5 3.5 0 0 0 1.6 1.6l.5-.6 1.2.4.1 1-.7.5C4.9 7.2 2.8 5.1 2.7 3.3z" fill="#fff"/></svg>031 555 27 40</p>
  </div>

  <div class="panel panel--2 services">
    <h2 class="services__title">Unsere<br>Dienstleistungen</h2>
    <ul class="services__list">
      <li class="service"><h3 class="service__name">Reguläre Besuchszeiten</h3><p class="service__text">Melden Sie Ihren Besuch bitte zwischen 7 und 8 Uhr morgens an, um die bestmögliche Betreuung zu gewährleisten</p></li>
      <li class="service"><h3 class="service__name">24/7 Grosstier-Notfalldienst</h3><p class="service__text">In tiermedizinischen Grosstier-Notfällen sind wir rund um die Uhr, an 7 Tagen pro Woche, für Sie da</p></li>
      <li class="service"><h3 class="service__name">Zahnsanierung mit modernster Technologie</h3><p class="service__text">Professionelle Zahnpflege für Ihre Tiere dank hochmoderner dentaler Röntgentechnologie</p></li>
      <li class="service"><h3 class="service__name">Ambulante Betreuung für Hühner</h3><p class="service__text">Besuchen Sie uns in der Sprechstunde für eine spezialisierte Geflügelversorgung</p></li>
    </ul>
    <p class="services__url">tierarztpraxis-lindenau.ch</p>
  </div>

  <div class="panel panel--3 care">
    <h2 class="care__title">Umfassende Betreuung für alle Arten von Tieren</h2>
    <ul class="care__list">
      <li class="care__item"><b>Kleintiere</b>: Hunde, Katzen, Nager, Hühner</li>
      <li class="care__item"><b>Nutztiere</b>: Rinder, Kühe, Schafe, Ziegen, Pferde</li>
    </ul>
  </div>
</section>

</body>
</html>
```